PEAK KENNEL - business card
A way to remember us and buy our products
Professional
PEAKKENNEL - the finest pick
Lindmarkv. 24
SE-712 46 Eskilstuna
SWEDEN
info@peakkennel-demo.se
www.peakkennel-demo.se
I would like the business cards and other material to match.
It is about dogs and our show trolley.
I need something to hand out as I meet people at dog shows or otherwise.
your ideas are welcome to figure out what the backside should be.
drawing of product_logo related
LOGO in whole, van be split into two
4 berth
LOGO PDF
drawing pdf
Product today. Steel 2 berth

```html
<!DOCTYPE html>
<html lang="en">
<head>
<meta charset="utf-8">
<title>PEAK KENNEL – Business Card</title>
<link href="https://fonts.googleapis.com/css2?family=Arimo:wght@400;700&display=swap" rel="stylesheet">
<style>
  :root {
    --backdrop: #e9e7e3;
    --card: #ffffff;
    --brand-blue: #1f5e9e;
    --accent-orange: #f39320;
    --ink: #1a1a1a;
    --rule: #c9c9c9;
  }
  * { margin: 0; padding: 0; box-sizing: border-box; }
  html, body {
    width: 1200px;
    height: 778px;
    overflow: hidden;
    background: var(--backdrop);
  }
  .card {
    position: absolute;
    left: 168px;
    top: 140px;
    width: 864px;
    height: 497px;
    background: var(--card);
    border-radius: 34px;
    box-shadow: 0 4px 14px rgba(0,0,0,0.12);
    font-family: "Arimo", Arial, sans-serif;
    color: var(--ink);
  }
  .brand {
    position: absolute;
    left: 84px;
    top: 88px;
    height: 96px;
    display: flex;
    align-items: center;
    gap: 44px;
  }
  .brand-dot {
    width: 96px;
    height: 96px;
    border-radius: 50%;
    background: var(--accent-orange);
    flex: none;
  }
  .brand-name {
    font-family: "Arimo", Arial, sans-serif;
    font-weight: 700;
    font-size: 72px;
    line-height: 1;
    color: var(--brand-blue);
    white-space: nowrap;
  }
  .holder {
    position: absolute;
    right: 485px;
    top: 296px;
    text-align: right;
  }
  .holder-name {
    font-weight: 700;
    font-size: 29px;
    line-height: 1.2;
  }
  .holder-position {
    font-weight: 700;
    font-size: 21px;
    line-height: 1.5;
  }
  .divider {
    position: absolute;
    left: 432px;
    top: 239px;
    width: 1.5px;
    height: 204px;
    background: var(--rule);
  }
  .address {
    position: absolute;
    left: 480px;
    top: 226px;
    font-size: 23px;
    line-height: 29px;
    list-style: none;
  }
  .contacts {
    position: absolute;
    left: 482px;
    top: 328px;
    list-style: none;
    font-size: 23px;
    line-height: 29px;
  }
  .contacts li {
    display: flex;
    align-items: center;
    gap: 9px;
  }
  .contacts svg {
    width: 16px;
    height: 16px;
    flex: none;
    fill: var(--accent-orange);
  }
</style>
</head>
<body>
  <main class="card">
    <div class="brand">
      <span class="brand-dot"></span>
      <span class="brand-name">PEAKKENNEL</span>
    </div>

    <div class="holder">
      <p class="holder-name">Your Name</p>
      <p class="holder-position">Position</p>
    </div>

    <div class="divider"></div>

    <ul class="address">
      <li>Lindmarkv. 24</li>
      <li>SE-712 46 Eskilstuna</li>
      <li>SWEDEN</li>
    </ul>

    <ul class="contacts">
      <li>
        <svg viewBox="0 0 16 16" aria-hidden="true"><rect x="4" y="1" width="8" height="14" rx="1.6"/><rect x="5.5" y="3" width="5" height="7" fill="#fff"/><circle cx="8" cy="12.5" r="1" fill="#fff"/></svg>
        <span>+46 70 1234567</span>
      </li>
      <li>
        <svg viewBox="0 0 16 16" aria-hidden="true"><rect x="1" y="3" width="14" height="10" rx="1"/><path d="M1.8 4 L8 9 L14.2 4" fill="none" stroke="#fff" stroke-width="1.4"/></svg>
        <span>info@peakkennel-demo.se</span>
      </li>
      <li>
        <svg viewBox="0 0 16 16" aria-hidden="true"><circle cx="8" cy="8" r="7"/><path d="M1 8 H15 M8 1 C4.5 4.5 4.5 11.5 8 15 M8 1 C11.5 4.5 11.5 11.5 8 15" fill="none" stroke="#fff" stroke-width="1"/></svg>
        <span>www.peakkennel-demo.se</span>
      </li>
    </ul>
  </main>
</body>
</html>
```